Plucky Pitch Banner for website:

We are doing up a banner for a Plucky Pitch Website on this wordpress theme: http://demo.brightloomthemes.com/compact/
Our theme for Plucky pitch is that - We exist to create enormously successful salespeople and savvy business people to take you them to the top!
Our logo is attached below and uses Trajan Font. You can either incorporate it or not (we don't mind either way as you see with the example banners they don't incorporate their logos at all).
We want the banner split into two sections, biggest part at the top with picture and this will also have writing in it which guides people to our newsletter (our main aim is to get people from the banner first look to sign up to our newsletter). The second part which is smaller will have the newsletter area/sign up.
Some favourite banners for ideas are:
- http://www.ellarowbeck.com/ - this this as what we want is similar to above, want to split ours like this to funnel people into our newsletter.
- www.wellnessuptown.com.au - we like this one as it has a picture but also writing
- http://corinnevallier.com/ - quite like this banner as it comes across to a very similar target market and looks professional
Was thinking the words something around: Believe you can be the best....? Open to other ideas.
I can send some photos if you like, but thought you might like to see what you would want to do before any photos went out. We have attached logo below and a social media arrow slide that we thought looked quite cool but it would have to be adjusted to the words Sales in the circle and words like customers, profit, money, margin, products, services in arrows. Not a must have but just a thought??? You guys are the gurus you normally come up with something very cool.
Target Market(s)
Our target market is Corporate sales people and teams, businesses (both new and existing to improve sales) and new business owners starting up businesses (especially women on how to sell) but really anyone wanting to know how to sell!!!
Industry/Entity Type
Business
Requirements
Must have
- Two sections, one part for picture to sell the idea to sign up to our newsletter, the other part for newsletter sign up

```html
<!DOCTYPE html>
<html lang="en">
<head>
<meta charset="utf-8">
<title>Plucky Pitch – Website Banner</title>
<link href="https://fonts.googleapis.com/css2?family=Cinzel:wght@400;600&family=Open+Sans:wght@400;700;800&family=Roboto+Slab:wght@300;400&display=swap" rel="stylesheet">
<style>
  :root {
    --backdrop: #0f2533;
    --page: #ffffff;
    --navy: #0b4569;
    --sky: #2e9ad6;
    --ink: #444444;
    --muted-band: #f6f6f6;
    --button-dark: #3d3d3d;
    --go-top: #7a8087;
    --go-bottom: #555b62;
    --photo-deep: #8fa9c2;
    --photo-mid: #c3d3e3;
    --photo-light: #e8eef4;
    --photo-white: #ffffff;
  }
  * { box-sizing: border-box; margin: 0; padding: 0; }
  html, body { width: 1200px; height: 1000px; overflow: hidden; }
  body { background: var(--backdrop); position: relative; font-family: "Open Sans", Arial, sans-serif; }

  .site { position: absolute; left: 40px; top: 180px; width: 1115px; height: 610px; background: var(--page); overflow: hidden; }

  .site-header { position: absolute; left: 0; top: 0; width: 100%; height: 67px; }
  .brand { position: absolute; left: 36px; top: 18px; display: flex; align-items: center; gap: 10px; }
  .brand-dot { width: 18px; height: 18px; border-radius: 50%; background: var(--sky); }
  .brand-name { font-family: "Cinzel", "Times New Roman", serif; font-weight: 600; font-size: 25px; color: var(--navy); letter-spacing: 0.3px; }

  .main-nav { position: absolute; top: 29px; left: 0; width: 100%; height: 20px; font-family: "Cinzel", "Times New Roman", serif; font-size: 12px; color: var(--ink); letter-spacing: 0.5px; }
  .main-nav span { position: absolute; top: 0; white-space: nowrap; }
  .nav-home { left: 664px; }
  .nav-about { left: 723px; }
  .nav-services { left: 794px; }
  .nav-solutions { left: 870px; }
  .nav-contacts { left: 956px; }

  .hero { position: absolute; left: 0; top: 67px; width: 100%; height: 368px; }
  .hero-photo { position: absolute; left: 0; top: 0; width: 830px; height: 100%;
    background:
      linear-gradient(180deg, rgba(255,255,255,0) 55%, rgba(120,140,165,0.25) 100%),
      linear-gradient(90deg, var(--photo-deep) 0%, var(--photo-mid) 35%, var(--photo-light) 75%, var(--photo-white) 100%); }

  .headline { position: absolute; left: 760px; top: 95px; color: var(--navy); font-weight: 800; }
  .headline-we { display: flex; align-items: flex-end; gap: 8px; }
  .headline-we .word { font-size: 46px; line-height: 40px; color: var(--sky); letter-spacing: -1px; }
  .headline-row { display: flex; align-items: center; margin-top: 2px; }
  .headline-keep { font-size: 84px; line-height: 74px; letter-spacing: -2px; }
  .headline-side { margin-left: 10px; color: var(--sky); font-weight: 700; font-size: 25px; line-height: 24px; }
  .headline-speed { font-size: 35px; line-height: 38px; letter-spacing: -0.5px; }

  .signup-band { position: absolute; left: 0; top: 435px; width: 100%; height: 62px; background: var(--sky); }
  .signup-prompt { position: absolute; left: 144px; top: 18px; color: #fff; font-weight: 700; font-size: 19px; letter-spacing: -0.3px; white-space: nowrap; }
  .field { position: absolute; top: 16px; height: 31px; background: #fff; border: 1px solid #9cc4de; font-family: Arial, sans-serif; font-size: 13px; color: #888; padding: 3px 7px; }
  .field-name { left: 573px; width: 155px; }
  .field-email { left: 738px; width: 218px; }
  .go-button { position: absolute; left: 964px; top: 15px; width: 77px; height: 33px; border-radius: 3px;
    background: linear-gradient(var(--go-top), var(--go-bottom)); color: #fff; font-weight: 700; font-size: 16px; text-align: center; line-height: 33px; }

  .intro-band { position: absolute; left: 0; top: 497px; width: 100%; height: 98px; background: var(--muted-band); }
  .intro-title { position: absolute; left: 108px; top: 28px; font-family: "Roboto Slab", Georgia, serif; font-weight: 300; font-size: 28px; color: var(--ink); white-space: nowrap; }
  .portfolio-button { position: absolute; left: 857px; top: 28px; width: 150px; height: 37px; border-radius: 3px; background: var(--button-dark);
    color: #fff; font-family: "Roboto Slab", Georgia, serif; font-size: 15px; text-align: center; line-height: 37px; white-space: nowrap; }
</style>
</head>
<body>
  <div class="site">
    <header class="site-header">
      <div class="brand"><span class="brand-dot"></span><span class="brand-name">Plucky Pitch</span></div>
      <nav class="main-nav">
        <span class="nav-home">Home</span><span class="nav-about">About</span><span class="nav-services">Services</span><span class="nav-solutions">Solutions</span><span class="nav-contacts">Contacts</span>
      </nav>
    </header>

    <section class="hero">
      <div class="hero-photo" role="img" aria-label="Photo of a smiling business team of four meeting around computer monitors in a bright office with window blinds"></div>
      <div class="headline">
        <div class="headline-we">
          <span class="word">we</span>
          <svg width="112" height="28" viewBox="0 0 112 28" aria-hidden="true">
            <g fill="#7d8b96">
              <rect x="2" y="14" width="4" height="12"/><rect x="8" y="8" width="4" height="18"/><rect x="14" y="3" width="4" height="23"/><rect x="0" y="26" width="20" height="2"/>
              <circle cx="39" cy="17" r="10"/><rect x="35" y="3" width="8" height="5" rx="1"/>
              <circle cx="60" cy="9" r="4"/><circle cx="72" cy="23" r="4"/><path d="M56 27 L72 3 L75 5 L59 29 Z"/>
              <rect x="86" y="1" width="22" height="27" rx="2"/>
            </g>
            <text x="39" y="21" font-size="11" font-family="Arial, sans-serif" font-weight="700" fill="#fff" text-anchor="middle">$</text>
            <g fill="#fff"><rect x="89" y="4" width="16" height="6"/>
              <rect x="89" y="13" width="4" height="3"/><rect x="95" y="13" width="4" height="3"/><rect x="101" y="13" width="4" height="3"/>
              <rect x="89" y="18" width="4" height="3"/><rect x="95" y="18" width="4" height="3"/><rect x="101" y="18" width="4" height="3"/>
              <rect x="89" y="23" width="4" height="3"/><rect x="95" y="23" width="4" height="3"/><rect x="101" y="23" width="4" height="3"/></g>
          </svg>
        </div>
        <div class="headline-row">
          <span class="headline-keep">KEEP</span>
          <span class="headline-side">YOUR<br>BUSINESS<br>UP TO</span>
        </div>
        <div class="headline-speed">SPEED ON MARKET</div>
      </div>
    </section>

    <section class="signup-band">
      <p class="signup-prompt">BELIEVE YOU CAN BE THE BEST? FIND OUT!!!</p>
      <div class="field field-name">First name</div>
      <div class="field field-email">e-mail*</div>
      <div class="go-button">GO!</div>
    </section>

    <section class="intro-band">
      <h2 class="intro-title">A Responsive HTML5 Theme</h2>
      <div class="portfolio-button">View my Portfolio</div>
    </section>
  </div>
</body>
</html>
```